Guarding One's Body Using Sharp Steel Cover

Hi we are producing a self defense course entitled Guarding One's Body Using Sharp Steel: A Complete Manual For Learning The Finest And Handiest Wilderness Tool In Recorded History.

I listed this as a book cover but it will actually be a DVD set, but the book cover model works fine.

See below for design examples - I am thinking we need a cover that will appeal to military/survival type people.

Target Market(s)

survivalists, cops, preppers, gun owners, martial artists, and average people wanting to learn how to defend themselves

Industry/Entity Type

Defense

Requirements
Must have
• Title: GUARDING ONE'S BODY USING SHARP STEEL: A COMPLETE MANUAL FOR LEARNING THE FINEST AND HANDIEST WILDERNESS TOOL IN RECORDED HISTORY
Nice to have
• Please look at these sample designs from other books as a model:
• https://files.plorvexa.org/media/en/4/27/BrindelQXMP.jpg - This stye is ideal.
• Other good examples:
• https://pics2.talvorn.com/8143907_k370.jpg
• http://m.zephquill.com/titles/2719058463k/48071935.jpg
• http://img.crondelmart.com/pics/P/73Tm58QyzFr._BX_KL410_TR316,410_.jpg
• http://3.cdn.wendoplix.net/-RTyZWLMMKAQ/BNWq_hufxaT/BBBBBBBBv8G/DKNp815ZaXW/s1600/Q4710392.JPG

```html
<!DOCTYPE html>
<html lang="en">
<head>
<meta charset="utf-8">
<title>Guarding One's Body Using Sharp Steel — Cover</title>
<link rel="stylesheet" href="https://fonts.googleapis.com/css2?family=Big+Shoulders+Stencil+Display:wght@900&family=Roboto+Condensed:wght@700&display=swap">
<style>
  :root {
    --cover-grey: #6d6e70;
    --ink-black: #121212;
    --chalk-white: #f1f1f1;
    --muted-grey: #a9abae;
    --blade-silver: #cfd3d6;
    --handle-black: #161616;
  }
  html, body {
    margin: 0;
    padding: 0;
    width: 841px;
    height: 1200px;
    overflow: hidden;
    background: var(--cover-grey);
  }
  .cover {
    position: relative;
    width: 841px;
    height: 1200px;
    background: var(--cover-grey);
    overflow: hidden;
  }
  .title-art {
    position: absolute;
    left: 0;
    top: 0;
    width: 841px;
    height: 705px;
  }
  .title-art text,
  .author-art text {
    font-family: "Big Shoulders Stencil Display", "Stardos Stencil", sans-serif;
    font-weight: 900;
  }
  .title-dark { fill: var(--ink-black); }
  .title-light { fill: var(--chalk-white); }

  .knife-visual {
    position: absolute;
    left: 0;
    top: 712px;
    width: 800px;
    height: 92px;
    border-radius: 0 0 0 0;
    background:
      linear-gradient(to bottom, rgba(109,110,112,0) 0%, rgba(109,110,112,0) 70%, rgba(109,110,112,0.5) 100%),
      linear-gradient(to right, var(--handle-black) 0%, var(--handle-black) 16%, #8d9094 19%, var(--blade-silver) 24%, var(--blade-silver) 82%, var(--cover-grey) 100%);
  }

  .subtitle {
    position: absolute;
    left: 0;
    top: 846px;
    width: 841px;
    margin: 0;
    text-align: center;
    font-family: "Roboto Condensed", "Arial Narrow", sans-serif;
    font-weight: 700;
    font-size: 33px;
    line-height: 56px;
    letter-spacing: 0.13em;
    color: var(--chalk-white);
    text-transform: uppercase;
  }
  .subtitle .line { display: block; }
  .subtitle .soft { color: var(--muted-grey); }

  .author-art {
    position: absolute;
    left: 0;
    top: 1100px;
    width: 841px;
    height: 70px;
  }
</style>
</head>
<body>
<main class="cover">
  <svg class="title-art" viewBox="0 0 841 705" aria-labelledby="cover-title">
    <defs>
      <filter id="worn-ink" x="0" y="0" width="100%" height="100%">
        <feTurbulence type="fractalNoise" baseFrequency="0.85" numOctaves="2" seed="7" result="noise"/>
        <feColorMatrix in="noise" type="matrix"
          values="0 0 0 0 0
                  0 0 0 0 0
                  0 0 0 0 0
                  0 0 0 -9 4.6" result="specks"/>
        <feComposite in="SourceGraphic" in2="specks" operator="out"/>
      </filter>
    </defs>
    <title id="cover-title">Guarding One's Body Using Sharp Steel</title>
    <g filter="url(#worn-ink)">
      <text class="title-dark" x="41" y="122" font-size="101" textLength="540" lengthAdjust="spacingAndGlyphs">GUARDING ONE'S</text>
      <text class="title-dark" x="41" y="315" font-size="226" textLength="630" lengthAdjust="spacingAndGlyphs">BODY</text>
      <text class="title-dark" x="41" y="483" font-size="192" textLength="760" lengthAdjust="spacingAndGlyphs">USING SHARP</text>
      <text class="title-light" x="41" y="692" font-size="222" textLength="753" lengthAdjust="spacingAndGlyphs">STEEL</text>
    </g>
  </svg>

  <div class="knife-visual" role="img" aria-label="Chef's knife with black handle and silver blade lying horizontally, casting a soft shadow"></div>

  <p class="subtitle">
    <span class="line">A Complete Manual</span>
    <span class="line soft">For Learning The Finest</span>
    <span class="line">And Handiest Wilderness</span>
    <span class="line">Tool <span class="soft">In Recorded History</span></span>
  </p>

  <svg class="author-art" viewBox="0 0 841 70" aria-label="Grant R Halloway">
    <text class="title-dark" x="420.5" y="54" text-anchor="middle" font-size="44" textLength="442" lengthAdjust="spacingAndGlyphs" filter="url(#worn-ink)">GRANT R HALLOWAY</text>
  </svg>
</main>
</body>
</html>
```